MD Trailcraft & Wildland Fair

I need a 1 page flyer for promotion of an upcoming sportsman and outdoor show(expo). would like the flyer to be able to be printed in B&W and color! show will include all things to do with the out doors, hunting fishing boating hiking atv camping rvs motorcycles. the event will have a kids zone, events games and activities for kids. there will be vendors showing the newest products. guest speakers and industry experts giving training and advice. this show will have something for everyone. food trucks and concessions. 200+ vendors. waterfould calling competition. deer/buck scoring casting competition for kids 3D Archery competitions

Target Market(s)

anyone event open to all ages!

Colors
ec1f27
000000
fbed22

Requirements
Must have
• date- september 1-2 2018
• location Pelling valley expo 4837 orchardmill rd east calverton MD 21652
• facebook - mdtrailcraftfair
• email mdtrailcraftfair@quorvex.com
• web www.mdtrailcraftfair.com
• vendor spaces still available! sign up now space going fast
Nice to have
• would like some thing that can be both printed in B&W and Color, and still have a great affect.
Should not have
• open to any suggestions

```html
<!DOCTYPE html>
<html lang="en">
<head>
<meta charset="utf-8">
<title>Maryland Trailcraft &amp; Wildland Fair</title>
<link rel="stylesheet" href="https://fonts.googleapis.com/css2?family=Tinos:wght@700&family=Oswald:wght@300;600&family=Arimo:ital,wght@0,700;1,400&display=swap">
<style>
  :root {
    --red: #ec1f27;
    --black: #000000;
    --yellow: #fbed22;
    --white: #ffffff;
    --ink: #1a1a1a;
  }
  * { margin: 0; padding: 0; box-sizing: border-box; }
  html, body { width: 786px; height: 1200px; overflow: hidden; background: var(--black); }
  .flyer { position: relative; width: 786px; height: 1200px; background: var(--black); overflow: hidden; }
  .hero { position: absolute; left: 0; top: 0; width: 786px; height: 600px; }
  .badge {
    position: absolute; left: 38px; top: 42px; width: 186px; height: 186px;
    border-radius: 50%; background: var(--red);
    display: flex; align-items: center; justify-content: center;
  }
  .badge-inner {
    width: 154px; height: 154px; border-radius: 50%; background: var(--white);
    display: flex; flex-direction: column; align-items: center; justify-content: center;
    font-family: "Tinos", serif; font-weight: 400; color: var(--ink); font-size: 31px; line-height: 1.15;
  }
  .title {
    position: absolute; left: 120px; top: 214px; width: 660px; text-align: right;
    font-family: "Tinos", serif; font-weight: 700; color: var(--red);
    font-size: 44px; line-height: 52px; letter-spacing: 0.5px;
    text-shadow: 2px 2px 0 #5a0c10, -1px -1px 0 #7a1015;
  }
  .title span { display: block; }
  .title .line-two { margin-right: 60px; text-align: center; padding-left: 120px; }
  .inset-frame {
    position: absolute; left: 7px; top: 330px; width: 420px; height: 238px; background: var(--red);
  }
  .inset-photo {
    position: absolute; left: 12px; top: 12px; width: 396px; height: 214px;
    background: linear-gradient(180deg, #2f6fc0 0%, #8cb4e2 55%, #c08a3c 72%, #7a4f1e 100%);
  }
  .date-band {
    position: absolute; left: 8px; top: 579px; width: 672px; height: 104px; background: var(--red);
    color: var(--white); text-align: center; padding-top: 6px;
  }
  .date { font-family: "Oswald", sans-serif; font-weight: 600; font-size: 23px; line-height: 30px; }
  .hours { font-family: "Oswald", sans-serif; font-weight: 300; font-size: 15px; line-height: 22px; letter-spacing: 0.5px; }
  .venue { font-family: "Tinos", serif; font-weight: 700; font-size: 13px; line-height: 20px; letter-spacing: 0.3px; }
  .welcome { font-family: "Arimo", sans-serif; font-style: italic; font-size: 13px; line-height: 18px; }
  .vendor-box {
    position: absolute; left: 264px; top: 740px; width: 522px; height: 81px; background: var(--yellow);
    text-align: center; font-family: "Arimo", sans-serif; font-weight: 700; padding-top: 2px;
  }
  .vendor-head { color: var(--red); font-size: 31px; line-height: 36px; }
  .vendor-social { color: var(--ink); font-size: 17px; line-height: 22px; }
  .vendor-web { color: var(--ink); font-size: 13px; line-height: 18px; }
  .features {
    position: absolute; left: 0; top: 902px; width: 786px; text-align: center;
    font-family: "Arimo", sans-serif; font-weight: 700; color: var(--white); font-size: 19px; line-height: 25px;
  }
  .features .free { color: var(--red); }
  .activity-band { position: absolute; left: 8px; top: 1124px; width: 778px; height: 76px; background: var(--yellow); }
</style>
</head>
<body>
<main class="flyer">
  <svg class="hero" viewBox="0 0 786 600" width="786" height="600">
    <defs>
      <linearGradient id="dusk" x1="0" y1="0" x2="0" y2="1">
        <stop offset="0" stop-color="#f0b98a"/>
        <stop offset="0.45" stop-color="#e3b08d"/>
        <stop offset="0.62" stop-color="#9c8f8c"/>
        <stop offset="1" stop-color="#4e4a4f"/>
      </linearGradient>
    </defs>
    <path class="swoosh" d="M8,248 C190,110 450,20 786,48 L786,370 C690,490 560,575 420,590 L8,590 Z" fill="var(--red)"/>
    <path class="scene" role="img" aria-label="Angler casting a bent rod over open water at sunset"
          d="M8,302 C200,150 470,72 786,92 L786,352 C690,468 560,556 420,575 L8,575 Z" fill="url(#dusk)"/>
  </svg>

  <div class="badge"><div class="badge-inner"><span>1ST</span><span>ANNUAL</span></div></div>

  <h1 class="title"><span>MARYLAND TRAILCRAFT</span><span class="line-two">&amp; WILDLAND FAIR</span></h1>

  <div class="inset-frame">
    <div class="inset-photo" role="img" aria-label="Hunter in camouflage aiming a shotgun over a golden marsh under blue sky"></div>
  </div>

  <section class="date-band">
    <p class="date">SEPTEMBER 1 &amp; 2, 2018</p>
    <p class="hours">SATURDAY 10-8&nbsp;&nbsp; SUNDAY 9-5</p>
    <p class="venue">PELLING VALLEY EXPO&nbsp;&nbsp; ROUTE 418 &amp; ROUTE 57</p>
    <p class="welcome">Everyone Welcome! Bring the Kids to the Special “Kids Zone”</p>
  </section>

  <section class="vendor-box">
    <p class="vendor-head">Vendors Spaces Still Available</p>
    <p class="vendor-social">Find Us on Fernpost.com/mdtrailcraftfair</p>
    <p class="vendor-web">www.mdtrailcraftfair.com/mdtrailcraftfair@quorvex.com</p>
  </section>

  <section class="features">
    <p>Dear &amp; Bear Scoring with Bucks-Bears-Stags (Bring Your Racks &amp; Skulls)</p>
    <p>Waterfowl Calling Contest, Casting Competitions (Kids Zone)</p>
    <p><span class="free">Free</span> Seminars, Displays, Hunting &amp; Fishing Outfitters,</p>
    <p>Archery &amp; Guns, Fresh &amp; Saltwater Vendors, Boats, ATV &amp; UTVs</p>
    <p>Food &amp; Music</p>
  </section>

  <svg class="activity-band" viewBox="0 0 778 76" width="778" height="76">
    <text x="24" y="51" textLength="738" lengthAdjust="spacingAndGlyphs"
          font-family="Oswald, sans-serif" font-weight="600" font-size="31" fill="var(--red)">BIKING I HIKING I HUNTING I FISHING I BOATING I RVS I ATVS MOTORCYCLES I UTVS</text>
  </svg>
</main>
</body>
</html>
```